依頼詳細
チラシ配布のため、デザイン製作をお願いします。
パッとみて印象に残り、何が強みなのか解りやすくアピールできればと思います。
記載項目
こちらに使用して頂きたいテキストを添付ファイルにまとめました。

イラストなどを使用して印象に残るデザインを作成して頂けると助かります。
必要に応じてテキストを追加して頂いても問題ありませんので
宜しくお願い致します。

サイトURLが記載されてますが、リニューアル予定ですので
サイトのデザインは参考にしないようお願い致します。
サイズ
A4
ページ数
片面
希望イメージ
シンプル 複雑
単色 カラフル
暗い 明るい
日常 高級
遊び心 厳粛
未来的 伝統的
女性的 男性的
希望する色
水色系、緑系、黄・オレンジ系
納品ファイル
• 高解像度JPG (.jpg)
• イラストレーター形式 (.ai)
• フォトショップ形式 (.psd)
補足説明
■ 選んだ理由

希望のデザインでした。

■ 提案者全員のお礼・コメント

参加いただき感謝です。
ありがとうございます。

```html
<!DOCTYPE html>
<html lang="ja">
<head>
<meta charset="UTF-8">
<title>遺品整理 料金目安チラシ</title>
<link rel="stylesheet" href="https://fonts.googleapis.com/css2?family=Noto+Sans+JP:wght@400;500;700;900&family=M+PLUS+Rounded+1c:wght@700;800;900&display=swap">
<style>
  :root{
    --blue:#1f8fd6;
    --blue-dark:#1366a8;
    --blue-pale:#e3f2fc;
    --blue-row:#f2f9fe;
    --red:#e8281e;
    --green:#3fae49;
    --green-pale:#e9f6e6;
    --orange:#f39a1c;
    --yellow:#ffe34d;
    --ink:#333;
    --line:#b8dcf3;
  }
  *{box-sizing:border-box;margin:0;padding:0}
  html,body{width:846px;height:1200px;overflow:hidden;background:#fff}
  body{font-family:"Noto Sans JP",sans-serif;color:var(--ink)}
  .flyer{position:relative;width:846px;height:1200px;background:#fff}

  .title-band{position:absolute;left:0;top:22px;width:846px;height:44px;background:var(--blue);
    color:#fff;font-weight:900;font-size:25px;letter-spacing:1px;padding-left:32px;line-height:44px}
  .title-band .bracket{color:var(--yellow)}

  .price-table{position:absolute;left:30px;top:80px;width:786px;border-collapse:collapse;font-weight:700}
  .price-table th{background:var(--blue-dark);color:#fff;font-size:16px;height:30px;font-weight:700;border:1px solid #fff}
  .price-table td{height:56px;border-bottom:1px solid var(--line);text-align:center;font-size:17px}
  .price-table td.plan{background:var(--blue-pale);font-size:20px;color:#222;width:140px}
  .price-table td.price{color:var(--red);font-size:27px;font-family:"M PLUS Rounded 1c",sans-serif;font-weight:900;width:330px;letter-spacing:.5px}
  .price-table td.price small{font-size:18px;color:var(--ink)}
  .price-table tr:nth-child(even) td:not(.plan){background:var(--blue-row)}

  .combo{position:absolute;left:30px;top:560px;width:786px;height:250px;border:5px solid var(--green);background:var(--green-pale)}
  .combo-lead{position:absolute;left:22px;top:16px;font-size:20px;font-weight:900;color:var(--green);white-space:nowrap}
  .combo-lead em{font-style:normal;color:var(--orange)}
  .combo-name{position:absolute;left:18px;top:48px;width:330px;height:56px;background:var(--green);color:#fff;
    font-family:"M PLUS Rounded 1c",sans-serif;font-weight:900;font-size:38px;text-align:center;line-height:56px;letter-spacing:1px;white-space:nowrap;overflow:hidden}
  .combo-price{position:absolute;left:22px;top:112px;font-family:"M PLUS Rounded 1c",sans-serif;font-weight:900;font-size:58px;color:var(--red);white-space:nowrap;line-height:1.3}
  .combo-price span{font-size:28px}
  .combo-note{position:absolute;left:22px;top:198px;width:340px;font-size:10px;line-height:1.4;color:#555}
  .truck-art{position:absolute;left:370px;top:64px;width:220px;height:150px;border-radius:8px;background:linear-gradient(#d7effd,#bfe3f8)}
  .staff-art{position:absolute;left:650px;top:70px;width:110px;height:150px;border-radius:8px;background:linear-gradient(#d6efc8,#a9d98f)}
  .art-label{position:absolute;font-size:16px;font-weight:900;color:var(--ink);text-align:center;line-height:1.25}
  .plus{position:absolute;left:602px;top:110px}

  .coupon{position:absolute;left:30px;top:834px;width:786px;height:122px;border:3px dashed var(--blue);background:var(--blue-pale)}
  .coupon-tag{position:absolute;left:22px;top:24px;width:190px;height:46px;background:var(--blue-dark);color:#fff;font-size:24px;font-weight:900;text-align:center;line-height:46px}
  .coupon-valid{position:absolute;left:40px;top:80px;font-size:12px;color:#555}
  .coupon-off{position:absolute;left:240px;top:4px;font-family:"M PLUS Rounded 1c",sans-serif;font-weight:900;font-size:92px;color:var(--orange);line-height:1.15;white-space:nowrap}
  .coupon-off span{font-size:66px}
  .coupon-msg{position:absolute;left:590px;top:30px;font-size:20px;font-weight:700;color:var(--blue-dark);line-height:1.5}

  .footer{position:absolute;left:0;top:975px;width:846px;height:225px}
  .company-tagline{position:absolute;left:30px;top:20px;width:330px;background:var(--green);color:#fff;font-size:13px;font-weight:700;text-align:center;height:24px;line-height:24px}
  .company-name{position:absolute;left:30px;top:52px;font-size:30px;font-weight:900;color:var(--green);display:flex;align-items:center;gap:8px;white-space:nowrap}
  .company-name .dot{width:18px;height:18px;background:var(--green);border-radius:50%}
  .company-addr{position:absolute;left:30px;top:100px;font-size:10px;color:#555;line-height:1.6;width:340px}
  .cta{position:absolute;left:390px;top:20px;width:426px;height:30px;background:var(--red);border-radius:15px;color:#fff;font-size:17px;font-weight:900;text-align:center;line-height:30px}
  .tel{position:absolute;left:390px;top:54px;font-family:"M PLUS Rounded 1c",sans-serif;font-weight:900;font-size:50px;color:var(--blue-dark);letter-spacing:1px;white-space:nowrap}
  .url{position:absolute;left:560px;top:124px;font-size:14px;font-weight:700;color:#444}
  .bottom-bar{position:absolute;left:0;bottom:0;width:846px;height:40px;background:var(--green)}
</style>
</head>
<body>
<main class="flyer">
  <h1 class="title-band"><span class="bracket">【遺品整理】</span>間取り別の料金目安</h1>

  <table class="price-table">
    <thead><tr><th>間取り</th><th>料金相場</th><th>作業人数</th><th>作業時間</th></tr></thead>
    <tbody>
      <tr><td class="plan">1R・1K</td><td class="price">30,000<small>円〜</small> 80,000<small>円</small></td><td>1〜2名</td><td>1〜3時間</td></tr>
      <tr><td class="plan">1DK</td><td class="price">50,000<small>円〜</small>120,000<small>円</small></td><td>2〜3名</td><td>1〜4時間</td></tr>
      <tr><td class="plan">1LDK</td><td class="price">70,000<small>円〜</small>200,000<small>円</small></td><td>2〜4名</td><td>2〜6時間</td></tr>
      <tr><td class="plan">2DK</td><td class="price">90,000<small>円〜</small>250,000<small>円</small></td><td>2〜5名</td><td>2〜6時間</td></tr>
      <tr><td class="plan">2LDK</td><td class="price">120,000<small>円〜</small>300,000<small>円</small></td><td>3〜6名</td><td>3〜8時間</td></tr>
      <tr><td class="plan">3DK</td><td class="price">150,000<small>円〜</small>400,000<small>円</small></td><td>3〜7名</td><td>4〜10時間</td></tr>
      <tr><td class="plan">3LDK</td><td class="price">170,000<small>円〜</small>500,000<small>円</small></td><td>4〜8名</td><td>5〜12時間</td></tr>
      <tr><td class="plan">4LDK以上</td><td class="price">220,000<small>円〜</small>600,000<small>円</small></td><td>4〜10名</td><td>6〜15時間</td></tr>
    </tbody>
  </table>

  <section class="combo">
    <p class="combo-lead"><em>片付けから</em>清掃まで全てお任せ!</p>
    <p class="combo-name">コミコミパック</p>
    <p class="combo-price">150,000<span>円〜</span></p>
    <p class="combo-note">※地域・状況によりプランが変わります。<br>詳しくはお問い合わせください。</p>
    <div class="art-label" style="left:430px;top:14px">軽トラック<br>1台分の回収</div>
    <div class="truck-art" role="img" aria-label="荷物を積んだ軽トラックのイラスト"></div>
    <svg class="plus" width="40" height="40" viewBox="0 0 40 40" aria-hidden="true"><path d="M16 4h8v12h12v8H24v12h-8V24H4v-8h12z" fill="#3fae49"/></svg>
    <div class="art-label" style="left:660px;top:14px">清掃・<br>リフォーム</div>
    <div class="staff-art" role="img" aria-label="作業着姿のスタッフのイラスト"></div>
  </section>

  <section class="coupon">
    <p class="coupon-tag">割引クーポン券</p>
    <p class="coupon-valid">（有効期限：2021.0.00）</p>
    <p class="coupon-off">10<span>%OFF</span></p>
    <p class="coupon-msg">このチラシを<br>ご提示ください。</p>
  </section>

  <footer class="footer">
    <p class="company-tagline">心をこめて遺品整理</p>
    <p class="company-name"><span class="dot"></span>株式会社ニューリーフ</p>
    <p class="company-addr">〒000-0000 大阪府大阪市中央区見本町0-0-0<br>古物商許可 第000000000000号 ／ 営業時間 9:00〜18:00</p>
    <p class="cta">まずはお気軽にご相談ください!</p>
    <p class="tel">TEL.06-0000-0000</p>
    <p class="url">www.newleaf-example.jp</p>
    <div class="bottom-bar"></div>
  </footer>
</main>
</body>
</html>
```